BSC Flyer to attract applicants 11x17

Brightline Stagecraft Company provides crew for local concerts, filming, theater, and corporate events.
The flyer will be posted on bulletin boards at colleges with theater programs.
Our primary venues are historic theaters in downtown LA
Need a 11x17 poster to attract potential applicants/crew
I have attached a poster that one of our staff made that has all if the relevant info - but i know the poster can look much better than that. I have also attached many images and our logo. It is not necessary to use all of the images, or any of them. The two images of the theater interiors are the venues we operate so they would be the first to include. I can send additional info or images upon request. Thank you

Entertainment

• APPLY@BSCCREWHUB.LA

```html
<!DOCTYPE html>
<html lang="en">
<head>
<meta charset="UTF-8">
<title>Brightline Stagecraft Company – Open Positions</title>
<link href="https://fonts.googleapis.com/css2?family=Poppins:wght@400;500;600;700;800&display=swap" rel="stylesheet">
<style>
  :root {
    --page-bg: #dcdee3;
    --paper: #eef0f3;
    --night-top: #161b2b;
    --night-mid: #1f2c4f;
    --night-low: #2c4f98;
    --brand-blue: #2b5cc0;
    --letter-light: #e4e6ea;
    --ink: #15161a;
    --white: #ffffff;
  }
  * { margin: 0; padding: 0; box-sizing: border-box; }
  html, body {
    width: 1200px; height: 1200px; overflow: hidden;
    background: var(--page-bg);
    font-family: "Poppins", sans-serif;
  }
  .poster {
    position: absolute; left: 225px; top: 24px;
    width: 750px; height: 1152px;
    background: var(--paper);
    overflow: hidden;
  }
  .skyline {
    position: absolute; left: 0; top: 0; width: 750px; height: 456px;
    background: linear-gradient(180deg, var(--night-top) 0%, var(--night-mid) 55%, var(--night-low) 100%);
  }
  .brand {
    position: absolute; left: 0; top: 150px; width: 750px;
    display: flex; align-items: center; justify-content: center; gap: 12px;
    color: var(--white); font-weight: 600; font-size: 22px; letter-spacing: 0.5px;
  }
  .brand-dot { width: 16px; height: 16px; border-radius: 50%; background: var(--white); }
  .headline-open { position: absolute; left: 0; top: 0; width: 750px; height: 560px; }
  .headline-open text { font-family: "Poppins", sans-serif; font-weight: 800; font-size: 250px; }
  .positions-at {
    position: absolute; top: 594px; left: 0; width: 750px; text-align: center;
    font-weight: 600; font-size: 24px; letter-spacing: 7px; color: var(--ink);
  }
  .company-name {
    position: absolute; top: 634px; left: 0; width: 750px; text-align: center;
    font-weight: 700; font-size: 29px; color: var(--ink);
  }
  .company-name .accent { color: var(--brand-blue); }
  .intro {
    position: absolute; top: 680px; left: 100px; width: 550px; text-align: center;
    font-weight: 400; font-size: 15.5px; line-height: 1.4; color: var(--ink);
  }
  .gallery-band {
    position: absolute; left: 2px; top: 802px; width: 685px; height: 132px;
    background: var(--brand-blue);
  }
  .photo { position: absolute; border-radius: 12px; }
  .photo-venue-a {
    left: 79px; top: 761px; width: 219px; height: 224px;
    background: linear-gradient(160deg, #d98a2a 0%, #8c3a14 55%, #5a1a10 100%);
  }
  .photo-stage {
    left: 304px; top: 779px; width: 158px; height: 183px;
    background: radial-gradient(circle at 50% 30%, #dfe6ff 0%, #4a5fd0 35%, #10143a 100%);
  }
  .photo-venue-b {
    left: 468px; top: 761px; width: 216px; height: 224px;
    background: linear-gradient(170deg, #4a3b8a 0%, #b0582e 50%, #3b1e2a 100%);
  }
  .send-label {
    position: absolute; top: 1024px; left: 0; width: 750px; text-align: center;
    font-weight: 600; font-size: 19px; letter-spacing: 6px; color: var(--ink);
  }
  .apply-button {
    position: absolute; left: 203px; top: 1068px; width: 342px; height: 51px;
    background: var(--brand-blue); border-radius: 3px;
    display: flex; align-items: center; justify-content: center;
    color: var(--white); font-weight: 600; font-size: 18px;
  }
</style>
</head>
<body>
  <div class="poster">
    <div class="skyline" role="img" aria-label="Downtown Los Angeles skyline at night"></div>

    <div class="brand"><span class="brand-dot"></span>Brightline Stagecraft Company</div>

    <svg class="headline-open" viewBox="0 0 750 560" aria-label="Open">
      <defs>
        <clipPath id="clip-upper"><rect x="0" y="0" width="750" height="456"/></clipPath>
        <clipPath id="clip-lower"><rect x="0" y="456" width="750" height="104"/></clipPath>
      </defs>
      <g clip-path="url(#clip-upper)">
        <text x="0" y="456" fill="var(--letter-light)" textLength="700" lengthAdjust="spacingAndGlyphs">Open</text>
      </g>
      <g clip-path="url(#clip-lower)">
        <text x="0" y="456" fill="var(--brand-blue)" textLength="700" lengthAdjust="spacingAndGlyphs">Open</text>
      </g>
    </svg>

    <div class="positions-at">POSITIONS AT</div>
    <div class="company-name">BRIGHTLINE <span class="accent">STAGECRAFT</span> COMPANY</div>
    <p class="intro">We are looking for talented technicians to add to our roster of skilled professionals</p>

    <div class="gallery-band"></div>
    <div class="photo photo-venue-a" role="img" aria-label="Ornate historic theater interior with red stage curtain"></div>
    <div class="photo photo-stage" role="img" aria-label="Performer on a concert stage under spotlights"></div>
    <div class="photo photo-venue-b" role="img" aria-label="Historic theater auditorium with decorated proscenium"></div>

    <div class="send-label">SEND RESUME TO</div>
    <div class="apply-button">APPLY@BSCCREWHUB.LA</div>
  </div>
</body>
</html>
```